Animal Eye Clinic needs a Business card

We are a new veterinary ophthalmology practice (Tessaly Animal Eye Care) and we need a business card designed. We only see animal eyes - we are not a regular veterinary clinic. We already have a logo. We are looking for a professional, good looking business card to hand out to our clients. We are looking for something simple but professional and contemporary. Our logo is likely the only picture/graphic that needs to be on the card.
Updates

Contact Information for Business Card

Marisol Dunkley, BSc, DVM, MSc, DipACVO
Veterinary Ophthalmologist

Phone: 250.418.3097
Email: tessalyanimaleyecare@mailbrook.net
Website: tessalyanimaleyecare.net
Address: 1840 Pellworth Rd
Kelowna, BC, V4T 8M3

Colors

Designer to choose colors to be used in the design.

Requirements
Must have
• Our logo (attached)

```html
<!DOCTYPE html>
<html lang="en">
<head>
<meta charset="utf-8">
<title>Tessaly Animal Eye Care – Business Card</title>
<link rel="stylesheet" href="https://fonts.googleapis.com/css2?family=Roboto:wght@300;400;700&display=swap">
<style>
  :root {
    --teal: #1a95a6;
    --paper: #eeeeee;
    --navy: #2a2e37;
    --white: #ffffff;
    --backdrop: #d3cbcb;
  }
  * { box-sizing: border-box; margin: 0; padding: 0; }
  html, body { width: 1200px; height: 712px; overflow: hidden; }
  body {
    background: var(--backdrop);
    font-family: "Roboto", Arial, sans-serif;
    position: relative;
  }
  .card {
    position: absolute;
    top: 206px;
    width: 525px;
    height: 300px;
    overflow: hidden;
    box-shadow: 0 10px 24px rgba(0,0,0,.18);
  }
  .card--front { left: 50px; background: var(--teal); }
  .card--back { left: 625px; background: var(--navy); }
  .card svg.shape { position: absolute; inset: 0; }

  .brand {
    position: absolute;
    display: flex;
    align-items: center;
    gap: 10px;
    color: var(--teal);
    font-weight: 700;
    font-size: 17px;
    letter-spacing: .02em;
    text-transform: uppercase;
    white-space: nowrap;
  }
  .brand__dot {
    width: 34px; height: 34px;
    border-radius: 50%;
    background: var(--teal);
    flex: none;
  }
  .card--front .brand { left: 26px; top: 134px; }
  .card--back .brand { left: 70px; top: 88px; font-size: 22px; }
  .card--back .brand__dot { width: 44px; height: 44px; }

  .person {
    position: absolute;
    left: 232px; top: 12px;
    color: var(--white);
    white-space: nowrap;
  }
  .person__name { font-size: 24px; font-weight: 300; text-transform: uppercase; line-height: 1; }
  .person__name b { font-weight: 700; }
  .person__title { font-size: 11px; font-weight: 400; margin-top: 3px; }

  .icon {
    position: absolute;
    width: 30px; height: 30px;
    border-radius: 50%;
    background: var(--teal);
    border: 3px solid var(--white);
    display: flex; align-items: center; justify-content: center;
  }
  .icon svg { width: 14px; height: 14px; }

  .contact {
    position: absolute;
    color: var(--white);
    font-size: 12px;
    line-height: 1.3;
    white-space: nowrap;
  }
  .contact--phone { font-size: 17px; }

  .web-strip {
    position: absolute;
    left: 0; right: 0; top: 238px;
    padding-left: 150px;
    text-align: center;
    color: var(--white);
    font-size: 11px;
    letter-spacing: .03em;
  }
  .web-strip svg { display: block; margin: 0 auto 4px; width: 12px; height: 12px; }
</style>
</head>
<body>

<section class="card card--front" aria-label="Business card front">
  <svg class="shape" viewBox="0 0 525 300" width="525" height="300">
    <path fill="var(--paper)" d="M0,0 H60 C150,0 320,70 320,152 C320,225 250,285 130,300 H0 Z"/>
  </svg>

  <div class="brand"><span class="brand__dot"></span>Tessaly Animal Eye Care</div>

  <div class="person">
    <div class="person__name"><b>Marisol</b> Dunkley</div>
    <div class="person__title">Veterinary Ophthalmologist</div>
  </div>

  <span class="icon" style="left:175px;top:15px">
    <svg viewBox="0 0 16 16"><circle cx="8" cy="5" r="3.2" fill="#fff"/><path d="M2 15c0-4 3-6 6-6s6 2 6 6z" fill="#fff"/></svg>
  </span>
  <span class="icon" style="left:266px;top:68px">
    <svg viewBox="0 0 16 16"><rect x="1" y="3" width="14" height="10" fill="#fff"/><path d="M1 3l7 6 7-6" fill="none" stroke="var(--teal)" stroke-width="1.5"/></svg>
  </span>
  <span class="icon" style="left:305px;top:137px">
    <svg viewBox="0 0 16 16"><path fill="#fff" d="M4 1l3 3-2 2c1 2 3 4 5 5l2-2 3 3-2 3C7 15 1 9 1 3z"/></svg>
  </span>
  <span class="icon" style="left:287px;top:198px">
    <svg viewBox="0 0 16 16" fill="none" stroke="#fff" stroke-width="1.4"><circle cx="8" cy="8" r="6.5"/><ellipse cx="8" cy="8" rx="3" ry="6.5"/><path d="M1.5 8h13M3 4.5h10M3 11.5h10"/></svg>
  </span>
  <span class="icon" style="left:255px;top:233px">
    <svg viewBox="0 0 16 16"><path fill="#fff" d="M8 1a5 5 0 0 1 5 5c0 4-5 9-5 9S3 10 3 6a5 5 0 0 1 5-5z"/><circle cx="8" cy="6" r="2" fill="var(--teal)"/></svg>
  </span>

  <div class="contact" style="left:305px;top:75px">tessalyanimaleyecare@mailbrook.net</div>
  <div class="contact contact--phone" style="left:345px;top:141px">250 418 3097</div>
  <div class="contact" style="left:326px;top:205px">www.tessalyanimaleyecare.net</div>
  <div class="contact" style="left:294px;top:232px">1840 Pellworth Rd<br>Kelowna, BC, V4T 8M3</div>
</section>

<section class="card card--back" aria-label="Business card back">
  <svg class="shape" viewBox="0 0 525 300" width="525" height="300">
    <path fill="var(--teal)" d="M0,300 V268 C90,268 150,268 172,248 C192,226 212,212 262,212 H440 C490,212 525,236 525,236 V300 Z"/>
  </svg>

  <div class="brand"><span class="brand__dot"></span>Tessaly Animal Eye Care</div>

  <div class="web-strip">
    <svg viewBox="0 0 16 16" fill="none" stroke="#fff" stroke-width="1.4"><circle cx="8" cy="8" r="6.5"/><ellipse cx="8" cy="8" rx="3" ry="6.5"/><path d="M1.5 8h13"/></svg>
    www.tessalyanimaleyecare.net
  </div>
</section>

</body>
</html>
```